VONTRA - Visual Orbit Networked Trade Arrangement - business cards

3x3 inch business cards
full color
use attached logo with old business card info

VONTRA will design, integrate and manufacture equipment for you to create an engaging, impactful experience for you and your consumer.

MISSION
VONTRA creates content-rich, emotionally compelling, and experiential spaces for a wide range of environments. Helping people find their way, communicate important information, and create unique moment of impact in virtually any environment that communicate with users.

What
You name it we will develop it, from digital wayfinding signage, multimedia installations, user interfaces, in any environment. We strive to enrich the lives of people wherever they work, play, learn, shop, travel, or gather.

HOW
We plan, design, and build a diverse range of visual communication and information systems, to improve the human experience. Dedicated to a collaborative design process that puts user needs first. We work with your ideas to shape a unique user experience that orients, informs, educates and captivates.
Benefits
Improved customer experience
Improved Branding/recall
Sales Lift
Cost savings/efficiency
Ad revenue/ROI
Differentiator from competition
Reduce perceived wait times
Internal communication
Generate inquiries
Safety/security
Better compliance/display control
Responsiveness
Public information
WHERE
Shopping Malls, entertainment and hospitality destinations and other environments are using the tools and story-telling approaches to create more engaging, emotionally compelling and impactful interactions with their customers, guests and users.
Markets
Architectural
Corporate
Education
Entertainment
Exhibition
Government
Healthcare
Hospitality
Residential
Retail
Sports
Tourism
Transportation
Urban
Visitor Centers
Workplace

Target Market(s)

corporate B2B, see attached details

Industry/Entity Type

Digital Signage

Contact Information for Business Card

see personal details from Pellward business cards apply to new cards

but use

www.vontra-example.com
marla@vontra-example.com

Font styles to use
Other font styles liked:
• century gothic

Colors
0355a3
3277b5
85acd3
34a6d7
0692cd

Requirements
Must have
• existing logo
• want depth and impact from the cards.
• giant dice image on one side of card
• details on the front side of card
• scalable image so you read the words under the logo
• 3inch x 3inch size only
Nice to have
• watermark with big dice image on front or possibly on the back with the cull logo on top of watermark cube.
• same blue color font on logo as on the card
• could use word cloud on the back of card (these are our company values)
Should not have
• should not be blank 2nd side
• should not just/ only redo my attachments - they are only a concept not what I want that's why I am using your services to provide more creativity and better ideas.

```html
<!DOCTYPE html>
<html lang="en">
<head>
<meta charset="utf-8">
<title>VONTRA – Business Cards</title>
<link rel="stylesheet" href="https://fonts.googleapis.com/css2?family=Open+Sans:wght@300;400;600;700&display=swap">
<style>
  :root {
    --brand-deep: #08598d;
    --brand-ink: #0c5a96;
    --brand-mid: #3277b5;
    --brand-soft: #85acd3;
    --brand-pale: #d5e3ef;
    --paper: #ffffff;
    --text: #2b2b2b;
    --stage: #ecebea;
  }
  * { box-sizing: border-box; margin: 0; padding: 0; }
  html, body { width: 1200px; height: 970px; overflow: hidden; }
  body {
    background: var(--stage);
    font-family: "Open Sans", Arial, sans-serif;
    position: relative;
  }
  .card {
    position: absolute;
    top: 281px;
    width: 407px;
    height: 409px;
    border-radius: 16px;
    overflow: hidden;
    box-shadow: 0 3px 8px rgba(0,0,0,0.18);
  }
  .card--back { left: 215px; background: var(--brand-deep); }
  .card--front { left: 655px; background: var(--paper); }

  .card__halo {
    position: absolute;
    border-radius: 50%;
  }
  .card--back .card__halo {
    width: 300px; height: 300px;
    left: 230px; top: 40px;
    background: rgba(255,255,255,0.07);
  }
  .card--front .card__halo {
    width: 260px; height: 260px;
    left: -110px; top: 70px;
    background: var(--brand-pale);
    opacity: 0.7;
  }

  .wordmark {
    position: absolute;
    left: 22px;
    top: 170px;
    display: flex;
    align-items: center;
    gap: 16px;
  }
  .wordmark__dot {
    width: 78px; height: 78px;
    border-radius: 50%;
    background: var(--paper);
  }
  .wordmark__name {
    font-weight: 300;
    font-size: 48px;
    color: var(--paper);
    letter-spacing: 0.5px;
  }

  .details {
    position: absolute;
    left: 194px;
    top: 100px;
    color: var(--text);
  }
  .details__name {
    font-weight: 700;
    font-size: 19px;
    color: var(--brand-ink);
    line-height: 1.2;
  }
  .details__role {
    font-size: 13.5px;
    margin-top: 3px;
  }
  .details__company {
    font-weight: 700;
    font-size: 17px;
    color: var(--brand-ink);
    margin-top: 16px;
  }
  .details__address {
    font-size: 13.5px;
    line-height: 20px;
    margin-top: 1px;
  }
  .contact-list {
    list-style: none;
    margin-top: 22px;
    font-size: 13.5px;
    line-height: 21px;
  }
  .contact-list li { display: flex; align-items: center; gap: 6px; }
  .contact-list svg { width: 11px; height: 11px; fill: var(--brand-ink); flex: none; }
</style>
</head>
<body>
  <section class="card card--back" aria-label="Card back">
    <div class="card__halo"></div>
    <div class="wordmark">
      <span class="wordmark__dot"></span>
      <span class="wordmark__name">VONTRA</span>
    </div>
  </section>

  <section class="card card--front" aria-label="Card front">
    <div class="card__halo"></div>
    <div class="details">
      <h1 class="details__name">MARLA QUENBY</h1>
      <p class="details__role">Director, Digital Strategies</p>
      <h2 class="details__company">VONTRA</h2>
      <p class="details__address">418-22 harbour row lakeford<br>&nbsp;nr k2q7m4 northland</p>
      <ul class="contact-list">
        <li>
          <svg viewBox="0 0 24 24" aria-hidden="true"><path d="M6.6 10.8a15.1 15.1 0 0 0 6.6 6.6l2.2-2.2c.3-.3.7-.4 1-.2 1.1.4 2.3.6 3.6.6.6 0 1 .4 1 1V20c0 .6-.4 1-1 1A17 17 0 0 1 3 4c0-.6.4-1 1-1h3.5c.6 0 1 .4 1 1 0 1.3.2 2.5.6 3.6.1.3 0 .7-.2 1z"/></svg>
          555.014.2290
        </li>
        <li>
          <svg viewBox="0 0 24 24" aria-hidden="true"><path d="M2 5h20v14H2z M2 5l10 8 10-8" stroke="#fff" stroke-width="1.6"/></svg>
          marla@vontra-example.com
        </li>
        <li>
          <svg viewBox="0 0 24 24" aria-hidden="true"><circle cx="12" cy="12" r="11"/><path d="M7 8c2 0 3 1 3 3s2 2 2 4-1 3-1 4M15 4c0 2 2 3 4 3" stroke="#fff" stroke-width="1.6" fill="none"/></svg>
          www.vontra-example.com
        </li>
      </ul>
    </div>
  </section>
</body>
</html>
```